Orrowind Partners Business Card

Looking for a design for our business cards. Need to look corporate and outstanding. I have enclosed our logos for the company. Orrowind partners is an investment firm for high level clients looking for advisory in their investments. White background or black is good. We will like to double sided options maybe at the back with just the logo of the firm.

Example of the info for the business card:

Edric Salvo
Managing Director

Panama Phone +507 384 7165
Switzerland Phone +41 44 917 2638
mail@orrowind-partners.example
www.orrowind-partners.example

Industry/Entity Type

Investment

```html
<!DOCTYPE html>
<html lang="en">
<head>
<meta charset="utf-8">
<title>Orrowind Partners Business Card</title>
<link rel="stylesheet" href="https://fonts.googleapis.com/css2?family=Open+Sans:wght@400;600&display=swap">
<style>
  :root {
    --stage: #ece9e4;
    --navy: #1f2f7a;
    --navy-deep: #1a2266;
    --blue-light: #4456b3;
    --ink: #222222;
    --paper: #ffffff;
    --white: #ffffff;
  }
  * { margin: 0; padding: 0; box-sizing: border-box; }
  html, body {
    width: 1200px;
    height: 784px;
    overflow: hidden;
    background: var(--stage);
    font-family: "Open Sans", Arial, sans-serif;
  }
  .canvas {
    position: relative;
    width: 1200px;
    height: 784px;
  }
  .card {
    position: absolute;
    width: 540px;
    height: 309px;
    border-radius: 4px;
    box-shadow: 0 10px 28px rgba(0, 0, 0, 0.18);
    overflow: hidden;
  }
  .card--back {
    left: 40px;
    top: 238px;
  }
  .card-back__texture {
    position: absolute;
    inset: 0;
    background: linear-gradient(150deg, var(--blue-light) 0%, var(--navy) 55%, var(--navy-deep) 100%);
  }
  .card-back__brand {
    position: absolute;
    left: 0;
    right: 0;
    top: 50%;
    transform: translateY(-50%);
    text-align: center;
    color: var(--white);
    font-size: 30px;
    font-weight: 600;
    letter-spacing: 1px;
  }
  .card--front {
    left: 620px;
    top: 238px;
    background: var(--paper);
  }
  .card-front__brand {
    position: absolute;
    left: 34px;
    top: 38px;
    color: var(--navy);
    font-size: 26px;
    font-weight: 600;
    letter-spacing: 0.5px;
  }
  .holder {
    position: absolute;
    left: 34px;
    top: 150px;
  }
  .holder__name {
    color: var(--navy);
    font-size: 17px;
    font-weight: 600;
    line-height: 1.2;
  }
  .holder__role {
    color: var(--ink);
    font-size: 11px;
    margin-top: 2px;
  }
  .contact {
    position: absolute;
    left: 34px;
    top: 212px;
    list-style: none;
    color: var(--ink);
    font-size: 12.5px;
    line-height: 1.45;
  }
</style>
</head>
<body>
  <main class="canvas">
    <section class="card card--back" aria-label="Card back">
      <div class="card-back__texture" role="img" aria-label="Deep blue faceted triangle pattern background"></div>
      <div class="card-back__brand">Orrowind Partners</div>
    </section>

    <section class="card card--front" aria-label="Card front">
      <div class="card-front__brand">Orrowind Partners</div>
      <div class="holder">
        <p class="holder__name">Edric Salvo</p>
        <p class="holder__role">Managing Director</p>
      </div>
      <ul class="contact">
        <li>Panama Phone +507 384 7165</li>
        <li>Switzerland Phone +41 44 917 2638</li>
        <li>mail@orrowind-partners.example</li>
        <li>www.orrowind-partners.example</li>
      </ul>
    </section>
  </main>
</body>
</html>
```